Quillby Housecrafters Door Hanger design, Postcard and presentation folders Design

we are a home improvement company in Portland Oregon, are main service is roofing but we also do gutters, painting and pressure washing. we are a certified roofing contractor for TRV. We have over 20years of experince in the roofing industry we use top quality materials. Our mission is to do quality work and provide the best service.
Updates

This door hangers are going to be share to homeowners where we are currently working at! I will like to have a square maybe 2 inch wide and 1 inch hide (blank) for me to put the address where we are working at. So we want to give a direct message to homeowners who we are and why we are there for. Our services are roofing, gutters, painting, and pressure washing. But 95% of the door hangers should give the message that we are a roofing contractor. We are also certified by TRV which means all of our new roof projects have a 50 year warranty which only 2% of roofing contractor can offer that. We also offer finance, and all quality work. I will like to add photos of our trucks since all of them are wrap which will build them trust.

Target Market(s)

This door hangers should be custom for Homeowners with residential Homes,,, Average customer are between 40 & 65 Years old.

Industry/Entity Type

Roofing

Contact Information for Business Card

Logo, name, phone number, credentials, and services like roofing gutters painting and pressure washing

Font styles to use
Serif
Sans Serif
Decorative

Colors
33b8a4
5c5c5c

Requirements
Must have
• I want tho have a folder design just like this business card sample i uploaded. Teal and charcoal with services ...
Nice to have
• company trucks, job photo, crew photo and credential photos
Should not have
• I dont want it too busy or crowded..

```html
<!DOCTYPE html>
<html lang="en">
<head>
<meta charset="utf-8">
<title>Quillby Housecrafters Door Hanger</title>
<link href="https://fonts.googleapis.com/css2?family=Oswald:wght@500;600&family=Lato:wght@400;700&display=swap" rel="stylesheet">
<style>
  :root {
    --stage: #c4c4c4;
    --paper: #ffffff;
    --teal: #41b3bb;
    --teal-deep: #26939a;
    --teal-text: #2e9ea0;
    --charcoal: #2f2f2f;
    --slate: #636363;
    --ink: #333333;
    --muted: #8a8a8a;
    --hole: #c4c4c4;
  }
  * { margin: 0; padding: 0; box-sizing: border-box; }
  html, body { width: 1200px; height: 1000px; overflow: hidden; background: var(--stage); }
  body { position: relative; font-family: "Lato", Arial, sans-serif; }

  .side-label {
    position: absolute; top: 62px; width: 200px; text-align: center;
    font-family: "Lato", Arial, sans-serif; font-size: 24px; color: #fff; letter-spacing: 0.5px;
  }
  .side-label--front { left: 281px; }
  .side-label--back { left: 719px; }

  .hanger { position: absolute; top: 137px; width: 335px; height: 783px; background: var(--paper); overflow: hidden; }
  .hanger--front { left: 215px; }
  .hanger--back { left: 650px; }

  .hang-hole { position: absolute; width: 118px; height: 118px; border-radius: 50%; background: var(--hole); left: 112px; top: 45px; z-index: 5; }

  .brand { position: absolute; left: 9px; top: 30px; display: flex; align-items: center; gap: 5px; }
  .brand__mark { width: 10px; height: 10px; background: var(--teal-deep); }
  .brand__name { font-family: "Oswald", sans-serif; font-weight: 600; font-size: 13px; line-height: 14px; color: var(--teal-deep); letter-spacing: 0.3px; }

  .hero-photo { position: absolute; left: 0; top: 115px; width: 335px; height: 200px;
    background: linear-gradient(180deg, #c9ccc9 0%, #6c6f5c 30%, #3f4449 60%, #2b2f36 100%); }

  .svg-layer { position: absolute; left: 0; top: 0; }

  .headline { position: absolute; left: 0; top: 330px; width: 335px; text-align: center;
    font-family: "Oswald", sans-serif; font-weight: 600; font-size: 29px; line-height: 34px; color: #fff; letter-spacing: 0.3px; }

  .section-title { position: absolute; font-family: "Oswald", sans-serif; font-weight: 600; font-size: 15px; color: var(--ink); letter-spacing: 0.2px; }
  .why-title { left: 24px; top: 449px; }
  .why-copy { position: absolute; left: 26px; top: 467px; width: 290px; font-weight: 700; font-size: 12.3px; line-height: 15px; color: var(--teal-text); }
  .promise-title { left: 28px; top: 573px; }
  .promise-copy { position: absolute; left: 28px; top: 593px; width: 275px; font-size: 9.4px; line-height: 12.2px; color: var(--muted); }

  .estimate-btn { position: absolute; left: 80px; top: 689px; width: 176px; height: 25px; border-radius: 8px;
    background: var(--teal); color: #fff; font-family: "Oswald", sans-serif; font-weight: 500; font-size: 15px; line-height: 25px; text-align: center; z-index: 3; }

  .contact { position: absolute; left: 0; width: 335px; text-align: center; font-size: 20px; line-height: 24px; z-index: 3; }
  .contact--phone { top: 719px; }
  .contact--web { top: 742px; }
  .contact svg { display: inline-block; vertical-align: -3px; margin-right: 3px; }
  .contact--light { color: #fff; }
  .contact--dark { color: var(--ink); }

  .back-top { position: absolute; left: 0; top: 0; width: 335px; height: 181px; background: var(--teal-deep); }
  .services { position: absolute; left: 0; top: 181px; width: 335px; height: 409px; background: var(--slate); }
  .services__title { position: absolute; top: 11px; width: 100%; text-align: center; font-family: "Oswald", sans-serif; font-weight: 600; font-size: 15px; color: #fff; }
  .service { position: absolute; width: 119px; }
  .service__photo { width: 119px; height: 97px; }
  .service__name { margin-top: 4px; text-align: center; font-weight: 700; font-size: 9px; color: #fff; letter-spacing: 0.2px; }
</style>
</head>
<body>
  <div class="side-label side-label--front">FRONT</div>
  <div class="side-label side-label--back">BACK</div>

  <section class="hanger hanger--front">
    <div class="brand">
      <span class="brand__mark"></span>
      <span class="brand__name">QUILLBY<br>HOUSECRAFTERS</span>
    </div>
    <div class="hang-hole"></div>
    <div class="hero-photo" role="img" aria-label="Photo of a house with a new dark shingle roof and gabled dormers"></div>

    <svg class="svg-layer" width="335" height="783" viewBox="0 0 335 783">
      <polygon points="0,314 335,297 335,404 0,421" fill="var(--teal)"/>
      <polygon points="0,711 335,693 335,783 0,783" fill="var(--charcoal)"/>
    </svg>

    <div class="headline">PORTLAND’S TOP-RATED<br>ROOFING COMPANY.</div>

    <h2 class="section-title why-title">WHY CHOOSE QUILLBY HOUSECRAFTERS?</h2>
    <p class="why-copy">Quillby Housecrafters is committed to providing our customers with the best quality products available. You can expect quality workmanship from our Certified Installers coupled with unrivaled honesty and integrity from start to finish!</p>

    <h2 class="section-title promise-title">OUR PROMISE</h2>
    <p class="promise-copy">Every roof we install comes with a 50 Year Non-Prorated Manufacture Warranty. All of TRV’s shingle products used by Quillby Housecrafters are covered by the Shield Plus warranty for 50 years. Under this warranty, TRV, at no charge, will repair or replace, at its option, any shingles proven to be defective for 50 years.</p>

    <div class="estimate-btn">REQUEST A FREE ESTIMATE</div>
    <div class="contact contact--phone contact--light">
      <svg width="14" height="18" viewBox="0 0 14 18"><path d="M3 1 L6 1 L7 5 L5 7 Q6 11 9 13 L11 11 L14 13 L13 17 Q5 17 1 8 Q0 3 3 1 Z" fill="var(--teal)"/></svg>(503) 555-0148
    </div>
    <div class="contact contact--web contact--light">
      <svg width="18" height="18" viewBox="0 0 18 18" fill="none" stroke="var(--teal)" stroke-width="1.5"><circle cx="9" cy="9" r="7.5"/><ellipse cx="9" cy="9" rx="3.5" ry="7.5"/><line x1="1.5" y1="9" x2="16.5" y2="9"/></svg>quillbyhousecrafters.com
    </div>
  </section>

  <section class="hanger hanger--back">
    <div class="back-top"></div>
    <div class="hang-hole"></div>
    <div class="services">
      <h2 class="services__title">OUR SERVICES</h2>
      <div class="service" style="left:36px; top:46px;">
        <div class="service__photo" role="img" aria-label="Roofer nailing shingles on a roof" style="background:linear-gradient(160deg,#d9dee3,#4a4d55 55%,#2d3035);"></div>
        <div class="service__name">ROOFING</div>
      </div>
      <div class="service" style="left:180px; top:46px;">
        <div class="service__photo" role="img" aria-label="Worker cleaning gutters" style="background:linear-gradient(180deg,#e2e6e8,#9aa0a2 55%,#5e564c);"></div>
        <div class="service__name">GUTTERS</div>
      </div>
      <div class="service" style="left:36px; top:167px;">
        <div class="service__photo" role="img" aria-label="Painter working on house siding" style="background:linear-gradient(135deg,#d6d9dc,#a9adb0 50%,#2a2d33);"></div>
        <div class="service__name">PAINTING</div>
      </div>
      <div class="service" style="left:180px; top:167px;">
        <div class="service__photo" role="img" aria-label="Worker pressure washing a driveway" style="background:linear-gradient(180deg,#b9bbb5,#7d8078 50%,#9a9a92);"></div>
        <div class="service__name">PRESSURE WASHING</div>
      </div>
      <div class="service" style="left:36px; top:287px;">
        <div class="service__photo" role="img" aria-label="Close-up of beige shingle siding" style="background:linear-gradient(180deg,#c9c3a6,#b3ad8e);"></div>
        <div class="service__name">SIDING</div>
      </div>
      <div class="service" style="left:180px; top:287px;">
        <div class="service__photo" role="img" aria-label="Roof deck with blue underlayment and attic vents" style="background:linear-gradient(170deg,#6d9fd0,#3f77b4 60%,#2c3d52);"></div>
        <div class="service__name">ATTIC VENTILATION</div>
      </div>
    </div>

    <div class="contact contact--phone contact--dark">
      <svg width="14" height="18" viewBox="0 0 14 18"><path d="M3 1 L6 1 L7 5 L5 7 Q6 11 9 13 L11 11 L14 13 L13 17 Q5 17 1 8 Q0 3 3 1 Z" fill="var(--teal)"/></svg>(503) 555-0148
    </div>
    <div class="contact contact--web contact--dark">
      <svg width="18" height="18" viewBox="0 0 18 18" fill="none" stroke="var(--teal)" stroke-width="1.5"><circle cx="9" cy="9" r="7.5"/><ellipse cx="9" cy="9" rx="3.5" ry="7.5"/><line x1="1.5" y1="9" x2="16.5" y2="9"/></svg>quillbyhousecrafters.com
    </div>
  </section>
</body>
</html>
```